Mossy Den Pet Supply

Thank you for your interest in this design contest. We are always welcome to questions and are looking forward to seeing what you can come up with.

We work on a Bootstrap platform with our custom built CMS. We require all designs to be sized accordingly with the bootstrap grid system found here: http://fernlattice.com/css/#grid

At the start of a competition, we are looking for general Home Page Design concepts and an example product grid page.

Homepage: Slide Show/Featured Products/Specials

example website as a reference:https://www.mintcollarworks.com/

Store Product Grid: Show a grid of product thumbnails. Included elements are thumbnail and price. Also included are filters (sort by, show by grid/list).

No photos at this time but Logo is attached. Looking for good quality photo's around the web. Please read the attached creative brief in depth to get an idea f what the client is looking for. Thanks!

```html
<!DOCTYPE html>
<html lang="en">
<head>
<meta charset="utf-8">
<title>Mossy Den Pet Supply</title>
<link href="https://fonts.googleapis.com/css2?family=Montserrat:wght@400;500;600;700&family=Lato:wght@300;400;700&display=swap" rel="stylesheet">
<style>
:root{
  --green:#74b72b;
  --ink:#2f2f2f;
  --muted:#8a8a8a;
  --body-text:#555555;
  --line:#e2e2e2;
  --cream:#f4f0e3;
  --cream-edge:#e2dbc5;
  --tan:#ece6d3;
  --footer:#f1f1f1;
  --white:#ffffff;
  --blue:#1da1e2;
  --icon-grey:#c4c4c4;
  --arrow-grey:#c9c9c9;
}
*{box-sizing:border-box;margin:0;padding:0}
html,body{width:1200px;height:2278px;overflow:hidden;background:var(--white)}
body{position:relative;font-family:'Lato',sans-serif;color:var(--ink)}

/* header */
.site-header{position:absolute;left:0;top:0;width:1200px;height:110px;background:var(--white);box-shadow:0 2px 4px rgba(0,0,0,.08);z-index:2}
.brand{position:absolute;left:137px;top:26px;display:flex;align-items:center;gap:8px}
.brand-mark{width:18px;height:18px;background:var(--green);flex:none}
.brand-name{font-family:'Montserrat',sans-serif;font-weight:700;color:var(--green);font-size:15px;line-height:18px;width:120px}
.main-nav a{position:absolute;top:61px;font-family:'Montserrat',sans-serif;font-weight:600;font-size:15px;color:var(--ink);text-decoration:none;white-space:nowrap}
.main-nav a.login{color:var(--green)}
.cart-summary{position:absolute;left:918px;top:14px;font-size:14px;color:var(--green);display:flex;align-items:center;gap:6px}

/* hero */
.hero{position:absolute;left:0;top:110px;width:1200px;height:498px;background:linear-gradient(100deg,#3b4a63 0%,#8c7a66 28%,#c9a57c 50%,#a4805c 72%,#6e5846 100%)}
.hero-title{position:absolute;right:138px;top:310px;font-family:'Montserrat',sans-serif;font-weight:700;font-size:46px;line-height:56px;color:var(--white);text-shadow:0 2px 6px rgba(0,0,0,.35);white-space:nowrap}

/* section titles */
.section-title{position:absolute;font-family:'Lato',sans-serif;font-weight:400;font-size:26px;line-height:32px;color:var(--ink)}

/* toolbar */
.sort-box{position:absolute;left:722px;top:646px;width:201px;height:30px;border:1px solid var(--line);font-size:13px;color:var(--muted);display:flex;align-items:center;padding-left:10px}
.sort-box b{color:var(--ink);font-weight:400;margin-left:4px}
.sort-box .caret{position:absolute;right:0;top:0;width:30px;height:28px;border-left:1px solid var(--line);display:flex;align-items:center;justify-content:center}
.view-label{position:absolute;left:940px;top:652px;font-size:13px;color:var(--muted)}
.view-btn{position:absolute;top:646px;width:30px;height:30px;border:1px solid var(--line);display:flex;align-items:center;justify-content:center}
.view-btn.active{background:var(--blue);border-color:var(--blue)}

/* product cards */
.product-card{position:absolute;top:695px;width:220px;height:314px;border:1px solid var(--line);background:var(--white)}
.product-thumb{height:147px;border-bottom:1px solid var(--line);display:flex;align-items:center;justify-content:center}
.product-thumb span{display:block;width:150px;height:100px;border-radius:8px}
.product-name{position:absolute;left:12px;top:156px;font-size:15px;color:var(--ink)}
.product-by{position:absolute;left:12px;top:178px;font-size:12px;color:var(--muted)}
.product-price{position:absolute;left:12px;top:196px;font-size:22px;font-weight:700;color:var(--green)}
.product-meta{position:absolute;left:0;top:228px;width:100%;height:48px;border-top:1px solid var(--line)}
.stars{position:absolute;left:12px;top:10px;font-size:17px;letter-spacing:1px;color:var(--green)}
.stars i{font-style:normal;color:#cfcfcf}
.reviews{position:absolute;right:12px;top:15px;font-size:11px;color:var(--muted)}
.product-actions{position:absolute;left:0;bottom:0;width:100%;height:38px;background:var(--tan);font-size:12px;color:var(--ink)}
.product-actions span{position:absolute;top:12px;display:flex;align-items:center;gap:6px}
.slider-arrow{position:absolute;top:816px;width:28px;height:28px;border-radius:50%;background:var(--arrow-grey);display:flex;align-items:center;justify-content:center}

/* specials */
.specials{position:absolute;left:0;top:1052px;width:1200px;height:251px;background:var(--cream)}
.special-card{position:absolute;top:84px;width:300px;height:106px;background:var(--white);border:8px solid var(--cream-edge);display:flex;align-items:center;padding-left:20px;gap:18px}
.special-card h3{font-family:'Montserrat',sans-serif;font-weight:400;font-size:26px;color:var(--green);line-height:28px;white-space:nowrap}
.special-card p{font-size:14px;color:var(--muted);margin-left:2px;white-space:nowrap}

/* news */
.news-photo{position:absolute;left:129px;top:1390px;width:462px;height:182px;background:linear-gradient(90deg,#6a4a34 0%,#9c6b3f 35%,#4a86b9 55%,#c47a3a 80%,#7a5a3c 100%)}
.news-headline{position:absolute;left:129px;top:1580px;font-family:'Montserrat',sans-serif;font-weight:500;font-size:17px;line-height:25px;color:var(--green);white-space:nowrap}
.news-date{position:absolute;left:129px;top:1636px;font-size:15px;line-height:18px;color:var(--muted)}
.news-text{position:absolute;left:129px;top:1667px;font-size:15px;line-height:23px;color:var(--body-text);white-space:nowrap}
.more-link{position:absolute;font-size:14px;font-weight:700;color:var(--green);white-space:nowrap}

/* events */
.event{position:absolute;left:610px;width:460px;height:66px}
.event-date{position:absolute;left:0;top:0;width:60px;height:66px;background:var(--green);color:var(--white);text-align:center;font-family:'Montserrat',sans-serif}
.event-date b{display:block;font-size:27px;line-height:36px;font-weight:600;border-bottom:2px solid var(--white)}
.event-date small{display:block;font-size:16px;line-height:28px}
.event-text{position:absolute;left:68px;top:4px;font-family:'Montserrat',sans-serif;font-weight:500;font-size:16px;line-height:24px;color:var(--ink);white-space:nowrap}

/* footer */
.site-footer{position:absolute;left:0;top:1791px;width:1200px;height:487px;background:var(--footer)}
.link-col{position:absolute;top:65px}
.link-col h4{font-size:15px;line-height:18px;font-weight:700;color:var(--green);margin-bottom:8px}
.link-col li{list-style:none;font-size:13px;color:var(--muted);line-height:30px}
.footer-brand{position:absolute;left:851px;top:42px;width:108px;height:117px;background:var(--white);border:1px solid var(--line);display:flex;flex-direction:column;align-items:center;justify-content:center;gap:8px}
.footer-brand .brand-name{font-size:14px;text-align:center;width:96px}
.contact{position:absolute;left:851px;top:168px;font-size:13px;line-height:24px;color:var(--muted)}
.contact a{color:var(--green);text-decoration:none}
.social{position:absolute;top:372px;left:471px;display:flex;gap:11px}
.social span{width:34px;height:34px;background:var(--icon-grey);border-radius:3px;display:block}
.social span.active{background:var(--blue)}
.copyright{position:absolute;left:0;top:432px;width:1200px;text-align:center;font-size:13px;color:var(--muted)}
</style>
</head>
<body>

<header class="site-header">
  <div class="brand"><span class="brand-mark"></span><span class="brand-name">Mossy Den<br>Pet Supply</span></div>
  <div class="cart-summary">
    <svg width="18" height="16" viewBox="0 0 18 16"><path d="M1 1h3l2 9h9l2-6H5" fill="none" stroke="#74b72b" stroke-width="1.8"/><circle cx="7" cy="13.5" r="1.5" fill="#74b72b"/><circle cx="14" cy="13.5" r="1.5" fill="#74b72b"/></svg>
    ( 03 ) items - $12,560
  </div>
  <nav class="main-nav">
    <a style="left:310px">Dogs</a>
    <a style="left:385px">Cats</a>
    <a style="left:458px">Our Story</a>
    <a style="left:570px">The Scoop</a>
    <a style="left:689px">Find a Retailer</a>
    <a style="left:841px">Become a Partner</a>
    <a class="login" style="left:1024px">Login</a>
  </nav>
</header>

<section class="hero" role="img" aria-label="Photo of a person relaxing on a sofa with a shaggy dog holding an orange ball">
  <h1 class="hero-title">We Know Their Needs</h1>
</section>

<h2 class="section-title" style="left:131px;top:630px">Featured Products</h2>
<div class="sort-box">Sort by: <b>Default Sorting</b>
  <span class="caret"><svg width="10" height="6"><path d="M1 1l4 4 4-4" fill="none" stroke="#888" stroke-width="1.5"/></svg></span>
</div>
<span class="view-label">View as:</span>
<span class="view-btn" style="left:996px"><svg width="12" height="10"><g fill="#999"><rect y="0" width="2" height="2"/><rect x="4" width="8" height="2"/><rect y="4" width="2" height="2"/><rect x="4" y="4" width="8" height="2"/><rect y="8" width="2" height="2"/><rect x="4" y="8" width="8" height="2"/></g></svg></span>
<span class="view-btn active" style="left:1039px"><svg width="12" height="12"><g fill="#fff"><rect width="5" height="5"/><rect x="7" width="5" height="5"/><rect y="7" width="5" height="5"/><rect x="7" y="7" width="5" height="5"/></g></svg></span>

<span class="slider-arrow" style="left:85px"><svg width="10" height="12"><path d="M7 1L2 6l5 5" fill="none" stroke="#fff" stroke-width="2"/></svg></span>
<span class="slider-arrow" style="left:1082px"><svg width="10" height="12"><path d="M3 1l5 5-5 5" fill="none" stroke="#fff" stroke-width="2"/></svg></span>

<article class="product-card" style="left:131px">
  <div class="product-thumb"><span role="img" aria-label="Patterned dog collar and leash" style="background:linear-gradient(135deg,#e86a8a,#5ab0e0)"></span></div>
  <div class="product-name">Aliquam suscipit</div><div class="product-by">By Elise Marchand</div><div class="product-price">$589.50</div>
  <div class="product-meta"><span class="stars">★★★★<i>★</i></span><span class="reviews">14 reviews</span></div>
  <div class="product-actions"><span style="left:10px"><svg width="12" height="12"><path d="M1 4h10l-1 8H2z M4 4V2h4v2" fill="#333" stroke="#333"/></svg>Add to cart</span><span style="left:144px"><svg width="12" height="12"><circle cx="6" cy="6" r="6" fill="#333"/><rect x="5.2" y="5" width="1.6" height="5" fill="#fff"/><rect x="5.2" y="2" width="1.6" height="1.6" fill="#fff"/></svg>Details</span></div>
</article>
<article class="product-card" style="left:370px">
  <div class="product-thumb"><span role="img" aria-label="Dog resting on a dark sofa-style pet bed" style="background:linear-gradient(180deg,#9a9a9a,#2e2e2e)"></span></div>
  <div class="product-name">Aliquam suscipit</div><div class="product-by">By Elise Marchand</div><div class="product-price">$589.50</div>
  <div class="product-meta"><span class="stars">★★★★<i>★</i></span><span class="reviews">14 reviews</span></div>
  <div class="product-actions"><span style="left:10px"><svg width="12" height="12"><path d="M1 4h10l-1 8H2z M4 4V2h4v2" fill="#333" stroke="#333"/></svg>Add to cart</span><span style="left:144px"><svg width="12" height="12"><circle cx="6" cy="6" r="6" fill="#333"/><rect x="5.2" y="5" width="1.6" height="5" fill="#fff"/><rect x="5.2" y="2" width="1.6" height="1.6" fill="#fff"/></svg>Details</span></div>
</article>
<article class="product-card" style="left:610px">
  <div class="product-thumb"><span role="img" aria-label="Bag of dry dog food" style="width:80px;height:120px;background:linear-gradient(180deg,#f2f2f2,#c23a2e 60%,#d8a24a)"></span></div>
  <div class="product-name">Aliquam suscipit</div><div class="product-by">By Elise Marchand</div><div class="product-price">$589.50</div>
  <div class="product-meta"><span class="stars">★★★★<i>★</i></span><span class="reviews">14 reviews</span></div>
  <div class="product-actions"><span style="left:10px"><svg width="12" height="12"><path d="M1 4h10l-1 8H2z M4 4V2h4v2" fill="#333" stroke="#333"/></svg>Add to cart</span><span style="left:144px"><svg width="12" height="12"><circle cx="6" cy="6" r="6" fill="#333"/><rect x="5.2" y="5" width="1.6" height="5" fill="#fff"/><rect x="5.2" y="2" width="1.6" height="1.6" fill="#fff"/></svg>Details</span></div>
</article>
<article class="product-card" style="left:851px">
  <div class="product-thumb"><span role="img" aria-label="Round brown plush pet bed" style="border-radius:50%;background:radial-gradient(ellipse,#c8a37c 30%,#5a3c28 70%)"></span></div>
  <div class="product-name">Aliquam suscipit</div><div class="product-by">By Elise Marchand</div><div class="product-price">$589.50</div>
  <div class="product-meta"><span class="stars">★★★★<i>★</i></span><span class="reviews">14 reviews</span></div>
  <div class="product-actions"><span style="left:10px"><svg width="12" height="12"><path d="M1 4h10l-1 8H2z M4 4V2h4v2" fill="#333" stroke="#333"/></svg>Add to cart</span><span style="left:144px"><svg width="12" height="12"><circle cx="6" cy="6" r="6" fill="#333"/><rect x="5.2" y="5" width="1.6" height="5" fill="#fff"/><rect x="5.2" y="2" width="1.6" height="1.6" fill="#fff"/></svg>Details</span></div>
</article>

<section class="specials">
  <h2 class="section-title" style="left:131px;top:22px">Specials</h2>
  <div class="special-card" style="left:129px">
    <svg width="42" height="42" viewBox="0 0 42 42"><path d="M4 16L16 4v8c14 0 22 8 22 26-4-10-10-14-22-14v8z" fill="#74b72b"/></svg>
    <div><h3>Free Return</h3><p>Free Return for 100 days</p></div>
  </div>
  <div class="special-card" style="left:450px">
    <svg width="46" height="36" viewBox="0 0 46 36"><rect x="2" y="4" width="26" height="20" fill="#74b72b"/><path d="M30 10h8l6 8v6H30z" fill="#74b72b"/><circle cx="10" cy="28" r="5" fill="#74b72b" stroke="#fff" stroke-width="2"/><circle cx="36" cy="28" r="5" fill="#74b72b" stroke="#fff" stroke-width="2"/></svg>
    <div><h3>Free Shipping</h3><p>Only for Our Special Offers</p></div>
  </div>
  <div class="special-card" style="left:769px">
    <svg width="44" height="44" viewBox="0 0 44 44"><polygon points="22,1 27,8 35,5 36,13 43,17 38,23 42,30 34,32 32,40 24,37 18,43 14,36 6,36 7,28 1,22 7,17 5,9 13,9 16,2" fill="#74b72b"/><text x="22" y="29" font-family="Montserrat,sans-serif" font-weight="700" font-size="17" fill="#fff" text-anchor="middle">%</text></svg>
    <div><h3>% Discount</h3><p>For Over $120</p></div>
  </div>
</section>

<h2 class="section-title" style="left:131px;top:1331px">Latest News</h2>
<div class="news-photo" role="img" aria-label="Photo of a child lying on a wooden deck beside a brown and white dog"></div>
<h3 class="news-headline">Lorem ipsum dolor sit amet, consectetuer adicing<br>elit, sed diam nonummy nibh euismod tincidu</h3>
<div class="news-date">April 22, 2014</div>
<p class="news-text">Duis autem vel eum iriure dolor in hendrerit in vulputate velit esse<br>molestie consequat, vel illum dolore eu feugiat nulla facilisis at<br>vero eros et accumsan</p>
<span class="more-link" style="left:129px;top:1740px">Read more »</span>

<h2 class="section-title" style="left:608px;top:1331px">Event Calendar</h2>
<div class="event" style="top:1390px"><div class="event-date"><b>20</b><small>May</small></div><p class="event-text">Lorem ipsum dolor sit amet, consectetuer<br>adicing elit, sed diam nonummy nibh</p></div>
<div class="event" style="top:1467px"><div class="event-date"><b>20</b><small>May</small></div><p class="event-text">Maecenas tempus, tellus eget condimen<br>tum rhoncus, sem quam semper libero</p></div>
<div class="event" style="top:1544px"><div class="event-date"><b>20</b><small>May</small></div><p class="event-text">Curabitur ligula sapien, tincidunt non,<br>euismod vitae, posuere imperdiet</p></div>
<div class="event" style="top:1620px"><div class="event-date"><b>20</b><small>May</small></div><p class="event-text">Lorem ipsum dolor sit amet, consectetuer<br>adicing elit, sed diam nonummy nibh</p></div>
<span class="more-link" style="left:610px;top:1697px">All Events »</span>

<footer class="site-footer">
  <div class="link-col" style="left:129px"><h4>Quick Links</h4><ul><li>Lorem ipsum dolor sit</li><li>Lconsectetuer adipiscing</li><li>Aenean commodo ligula</li><li>Aenean massa</li><li>Cum sociis natoque pe</li><li>Dmagnis dis parturient</li><li>Anascetur ridiculus mus</li></ul></div>
  <div class="link-col" style="left:369px"><h4>Quick Links</h4><ul><li>Lorem ipsum dolor sit</li><li>Lconsectetuer adipiscing</li><li>Aenean commodo ligula</li><li>Aenean massa</li><li>Cum sociis natoque pe</li><li>Dmagnis dis parturient</li><li>Anascetur ridiculus mus</li></ul></div>
  <div class="link-col" style="left:610px"><h4>Quick Links</h4><ul><li>Lorem ipsum dolor sit</li><li>Lconsectetuer adipiscing</li><li>Aenean commodo ligula</li><li>Aenean massa</li><li>Cum sociis natoque pe</li><li>Dmagnis dis parturient</li><li>Anascetur ridiculus mus</li></ul></div>
  <div class="footer-brand"><span class="brand-mark"></span><span class="brand-name">Mossy Den Pet Supply</span></div>
  <div class="contact">1480 W. Pinecrest Rd.,<br>Lakeford, MT 59000<br>Toll free: 1 (800) 555-0142<br>Local: (406) 555-0187<br>Fax: (406) 555-0193<br>Email: <a>office@mossydenpets.com</a></div>
  <div class="social"><span></span><span></span><span class="active"></span><span></span><span></span><span></span></div>
  <p class="copyright">© Mossy Den Pet Supply 2014. All Rights Reserved</p>
</footer>

</body>
</html>
```